We have a cheerleading competition on Sunday the 30 and I want to encourage parent assistance, support and participation!
Updates

1. Please add:
    Cheer Championship (instead of Cheerleading Competition)

2. Banner: Let's support our Cheerleaders!

Under Banner have the Date in big

Before the Location add:  Joins us at:

Thank you all for your designs and taking the time to submit them. I greatly appreciate them and they were all lovely. I could only pick one though! Hope to have you again on my next project.

Regards, Dariela

Requirements
Must have
• Flyer should be 1/2 of an A4 page. kid friendly. The cheerleaders are 6-13 yrs old.
The colors Burgundy, Gold (yellow) and White - It should have the team Eagle design on it. Bayview Ridge Otters

Simple design. It will contain an address, times and dates.

should have all of the following information:

Date: Sunday - October 30th 2011
Location: Harbor Crest Arena at the Coastal Pines College
3870 Pellman Lane
Coral gables, FL 33146
Time: Tickets on sale 8:30AM - Doors Open 9:00AM Starts: 10:00AM
Prices: Adults $10.00 Children $5.00 - Cash Only

```html
<!DOCTYPE html>
<html lang="en">
<head>
<meta charset="utf-8">
<title>Bayview Ridge Otters Cheer Championship</title>
<link rel="stylesheet" href="https://fonts.googleapis.com/css2?family=Alfa+Slab+One&family=Graduate&family=Lilita+One&family=Lobster&display=swap">
<style>
  :root {
    --burgundy: #8a1430;
    --burgundy-deep: #5e0a1f;
    --burgundy-bright: #b3213f;
    --gold: #f4b619;
    --gold-light: #ffd84a;
    --white: #ffffff;
  }
  * { margin: 0; padding: 0; box-sizing: border-box; }
  html, body { width: 852px; height: 1200px; overflow: hidden; background: var(--gold); }
  .flyer {
    position: relative;
    width: 852px; height: 1200px;
    background: var(--gold);
    padding: 19px;
  }
  .flyer-field {
    position: relative;
    width: 100%; height: 100%;
    overflow: hidden;
    background: radial-gradient(ellipse at 50% 42%, var(--burgundy-bright) 0%, var(--burgundy) 45%, var(--burgundy-deep) 100%);
  }
  .abs { position: absolute; }

  .team-name {
    left: 22px; top: 28px;
    font-family: "Lilita One", sans-serif;
    font-size: 50px; color: var(--gold-light);
    transform: rotate(-5deg);
    transform-origin: left bottom;
    letter-spacing: 1px;
  }
  .mascot-cheer {
    right: 8px; top: -2px; width: 160px; height: 165px;
    background: radial-gradient(ellipse at 50% 50%, var(--gold) 0%, rgba(244,182,25,0.3) 70%, transparent 72%);
  }

  .title-swoosh { left: 30px; top: 290px; width: 780px; height: 120px; }
  .title-cheer {
    left: 0; width: 100%; top: 108px; text-align: center;
    font-family: "Alfa Slab One", serif;
    font-size: 150px; line-height: 1;
    color: var(--burgundy);
    -webkit-text-stroke: 4px var(--white);
    paint-order: stroke fill;
    text-shadow: 0 0 0 var(--gold), 6px 6px 0 var(--gold), -6px -2px 0 var(--gold), 6px -2px 0 var(--gold), -6px 6px 0 var(--gold);
    letter-spacing: 2px;
    padding-left: 20px;
  }
  .title-champ {
    left: 0; width: 100%; top: 220px; text-align: center;
    font-family: "Lobster", cursive;
    font-size: 118px; line-height: 1;
    color: var(--burgundy);
    -webkit-text-stroke: 3px var(--white);
    paint-order: stroke fill;
    text-shadow: 5px 5px 0 var(--gold), -5px -3px 0 var(--gold), 5px -3px 0 var(--gold), -5px 5px 0 var(--gold);
    transform: rotate(-3deg);
  }

  .support {
    left: 0; width: 100%; text-align: center;
    font-family: "Graduate", serif;
    color: var(--white);
    text-shadow: 3px 3px 0 var(--gold), 6px 6px 0 var(--burgundy-deep);
  }
  .support-top { top: 406px; font-size: 64px; }
  .support-main { top: 482px; font-size: 86px; letter-spacing: 1px; }

  .event-date {
    left: 0; width: 100%; top: 580px; text-align: center;
    font-family: "Lilita One", sans-serif;
    font-size: 56px; color: var(--white);
  }
  .rule { height: 0; border-top: 4px dashed var(--gold); }
  .rule-a { left: 0; width: 100%; top: 668px; transform: rotate(-1.5deg); }
  .rule-b { left: 0; width: 100%; top: 712px; transform: rotate(-1.5deg); border-top-style: solid; border-top-width: 3px; }
  .join {
    left: 0; width: 100%; top: 670px; text-align: center;
    font-family: "Lilita One", sans-serif;
    font-size: 44px; color: var(--white);
  }
  .venue {
    left: 0; width: 100%; top: 732px; text-align: center;
    font-family: "Lilita One", sans-serif;
    font-size: 27px; line-height: 40px; color: var(--white);
  }
  .rule-c { left: 60px; width: 270px; top: 846px; border-top: 4px solid var(--gold); }
  .rule-d { left: 450px; width: 300px; top: 812px; border-top: 4px solid var(--gold); }

  .arrive {
    left: 14px; top: 870px;
    font-family: "Lilita One", sans-serif;
    font-size: 54px; color: var(--white);
  }
  .times {
    left: 465px; top: 830px;
    font-family: "Lilita One", sans-serif;
    font-size: 27px; line-height: 46px; color: var(--white);
  }

  .ticket-panel { left: 200px; top: 930px; width: 620px; height: 140px; }
  .ticket-sale {
    left: 232px; top: 938px;
    font-family: "Lilita One", sans-serif;
    font-size: 30px; color: var(--burgundy);
  }
  .ticket-price {
    left: 230px;
    font-family: "Graduate", serif;
    font-size: 34px; color: var(--burgundy);
  }
  .price-adult { top: 978px; }
  .price-child { top: 1022px; }
  .cash {
    left: 566px; top: 968px;
    font-family: "Lilita One", sans-serif;
    font-size: 42px; line-height: 44px; color: var(--white);
    text-shadow: 2px 2px 0 var(--burgundy);
  }

  .mascot-head {
    left: -10px; top: 985px; width: 210px; height: 140px;
    border-radius: 50% 40% 50% 40%;
    background: radial-gradient(ellipse at 55% 45%, #9c2a3c 0%, var(--burgundy-deep) 60%, #2a0610 100%);
    border: 4px solid var(--gold);
  }
  .rule-bottom { left: 0; width: 100%; top: 1138px; border-top: 4px dashed var(--gold); }
</style>
</head>
<body>
<div class="flyer">
  <div class="flyer-field">
    <div class="abs team-name">Bayview Ridge Otters</div>
    <div class="abs mascot-cheer" role="img" aria-label="Silhouette of a team cheerleader with pom-poms"></div>

    <svg class="abs title-swoosh" viewBox="0 0 780 120" aria-hidden="true">
      <path d="M30 10 C200 40 300 95 400 110 C500 95 640 40 760 0 L770 20 C650 70 520 120 400 120 C280 120 160 70 20 30 Z" fill="var(--gold)" stroke="var(--burgundy-deep)" stroke-width="3"/>
    </svg>
    <div class="abs title-cheer">CHEER</div>
    <div class="abs title-champ">Championship</div>

    <div class="abs support support-top">LET'S SUPPORT OUR</div>
    <div class="abs support support-main">CHEERLEADERS</div>

    <div class="abs event-date">Sunday - October 30th 2011</div>
    <div class="abs rule rule-a"></div>
    <div class="abs join">Join us at:</div>
    <div class="abs venue">Harbor Crest Arena @ The Coastal Pines College<br>3870 Pellman Lane Coral Gables, FL 33146</div>
    <div class="abs rule rule-c"></div>
    <div class="abs rule rule-d"></div>

    <div class="abs arrive">Arrive Early!!!</div>
    <div class="abs times">Doors Open 9:00AM<br>Starts: 10:00AM</div>

    <svg class="abs ticket-panel" viewBox="0 0 620 140" aria-hidden="true">
      <path d="M0 0 H520 L560 70 L520 140 H0 Z" fill="var(--gold)"/>
      <path d="M0 0 H520 L560 70 L520 140 H0 Z" fill="none" stroke="var(--gold-light)" stroke-width="3" transform="translate(6 6) scale(0.98)"/>
      <path d="M535 0 H560 L600 70 L560 140 H535 L575 70 Z" fill="var(--gold)"/>
      <path d="M575 0 H595 L635 70 L595 140 H575 L615 70 Z" fill="var(--gold)"/>
    </svg>
    <div class="abs ticket-sale">Tickets on Sale @ 8:30AM</div>
    <div class="abs ticket-price price-adult">ADULTS $10.00</div>
    <div class="abs ticket-price price-child">CHILDREN $5.00</div>
    <div class="abs cash">Cash<br>Only</div>

    <div class="abs mascot-head" role="img" aria-label="Team mascot emblem"></div>
    <div class="abs rule-bottom"></div>
  </div>
</div>
</body>
</html>
```